Kelvaro Pools

Luxury pool designer builder brochure

Company name is "Kelvaro"
Tag line is "Pools for the Mind Body & Soul"
Maybe integrate "Luxury Urban Lifestyle"

Target Market(s)

30 to 65 income of 200000.00 plus Affluent, high end life style
Luxury living

Industry/Entity Type

It Company

Font styles to use
Serif

Colors
000000

Requirements
Must have
• NOTE:
• Please remove the "Aquatic environments for the under the logo.
• I want a black background with a very contemporary feel.
• This is a luxury lifestyle product.

```html
<!DOCTYPE html>
<html lang="en">
<head>
<meta charset="utf-8">
<title>Kelvaro Pools – Luxury Urban Lifestyle</title>
<link rel="stylesheet" href="https://fonts.googleapis.com/css2?family=Questrial&display=swap">
<style>
  :root {
    --bg: #262626;
    --ink: #ffffff;
    --ink-soft: #e4e4e4;
    --title: #d9f3f1;
    --teal: #7fd3cf;
    --teal-deep: #3fb3b0;
    --silver: #c9cccc;
    --footer: #136f8c;
    --footer-edge: #8fd4d8;
    --font: "Questrial", "Century Gothic", sans-serif;
  }
  * { box-sizing: border-box; margin: 0; padding: 0; }
  html, body { width: 1030px; height: 1200px; overflow: hidden; background: var(--bg); }
  .flyer {
    position: relative;
    width: 1030px;
    height: 1200px;
    background: var(--bg);
    font-family: var(--font);
    color: var(--ink);
    overflow: hidden;
  }
  .flyer__shapes { position: absolute; inset: 0; }
  .tagline {
    position: absolute; top: 40px; left: 0; width: 100%;
    text-align: center; font-size: 46px; color: var(--title); letter-spacing: 0.5px;
  }
  .subline {
    position: absolute; top: 116px; left: 0; width: 100%;
    text-align: center; font-size: 27px; letter-spacing: 1.5px;
  }
  .brand-name {
    position: absolute; top: 375px; left: 0; width: 100%;
    text-align: center; font-size: 84px; letter-spacing: 3px; color: var(--ink);
  }
  .intro__heading {
    position: absolute; top: 648px; left: 0; width: 100%;
    text-align: center; font-size: 32px; font-weight: 400; color: var(--ink-soft);
  }
  .intro__rule {
    position: absolute; top: 697px; left: 88px; width: 860px; height: 1.5px;
    background: var(--teal-deep);
  }
  .intro__body {
    position: absolute; top: 716px; left: 44px; width: 944px;
    font-size: 17.6px; line-height: 23.5px; color: var(--ink-soft);
    text-align: justify;
  }
  .gallery__item { position: absolute; top: 880px; width: 278px; height: 167px; }
  .gallery__item--night { left: 46px; background: linear-gradient(180deg, #1f3a22 0%, #2f4a3a 45%, #4f6fc8 70%, #c9b9a0 100%); }
  .gallery__item--fire { left: 375px; background: linear-gradient(180deg, #6f8fb4 0%, #97a6b8 35%, #8a5b48 60%, #3b87a8 80%, #7a5a44 100%); }
  .gallery__item--lawn { left: 704px; background: linear-gradient(180deg, #5c7fa6 0%, #a8b7c8 45%, #9a7f6a 65%, #5f7a48 85%, #50703e 100%); }
  .contact {
    position: absolute; top: 1140px; left: 0; width: 100%;
    text-align: center; font-size: 22px; color: var(--ink); word-spacing: 1px;
  }
  .contact span { margin: 0 6px; }
</style>
</head>
<body>
<main class="flyer">
  <svg class="flyer__shapes" width="1030" height="1200" viewBox="0 0 1030 1200" aria-hidden="false">
    <defs>
      <linearGradient id="heroTones" x1="0" y1="0" x2="1" y2="1">
        <stop offset="0" stop-color="#2e3b2c"/>
        <stop offset="0.35" stop-color="#8a7f6c"/>
        <stop offset="0.55" stop-color="#3f86b4"/>
        <stop offset="0.8" stop-color="#a39a8a"/>
        <stop offset="1" stop-color="#5d6b52"/>
      </linearGradient>
    </defs>
    <path role="img" aria-label="Photo of a luxury home backyard at dusk with a long lit pool, fire bowls and landscaped terrace"
          d="M0,95 Q515,265 1030,95 L1030,660 Q515,440 0,660 Z" fill="url(#heroTones)"/>
    <path class="band band--top" d="M0,62 Q515,245 1030,62 L1030,95 Q515,265 0,95 Z" fill="var(--teal)" opacity="0.85"/>
    <path class="band-line" d="M0,95 Q515,265 1030,95" fill="none" stroke="var(--silver)" stroke-width="4"/>
    <path class="band band--bottom" d="M0,705 Q515,425 1030,705 L1030,660 Q515,440 0,660 Z" fill="var(--teal)" opacity="0.9"/>
    <path class="band-line" d="M0,660 Q515,440 1030,660" fill="none" stroke="var(--silver)" stroke-width="4"/>
    <path class="footer-band" d="M0,1151 Q515,1031 1030,1151 L1030,1200 L0,1200 Z" fill="var(--footer)"/>
    <path class="footer-edge" d="M0,1151 Q515,1031 1030,1151" fill="none" stroke="var(--footer-edge)" stroke-width="5"/>
  </svg>

  <h1 class="tagline">Pools for the Mind Body &amp; Soul</h1>
  <p class="subline">LUXURY URBAN LIFESTYLE</p>
  <p class="brand-name">Kelvaro</p>

  <section class="intro">
    <h2 class="intro__heading">Your pool is waiting for you to get started</h2>
    <div class="intro__rule"></div>
    <p class="intro__body">Kelvaro Pools and Outdoors are known for their innovation and excellence in swimming pool design and construction, having been recognized by their peers with many awards. Kelvaro have been designing and building custom pools and outdoor living area’s for over 15 years and has built a reputation for excellence in custom luxury swimming pool design / outdoor living space, planning and construction. As a premium choice Houston pool builder and designer, many of the preeminent homes in the Houston area feature our pools and outdoor living spaces.</p>
  </section>

  <section class="gallery">
    <div class="gallery__item gallery__item--night" role="img" aria-label="Photo of a free-form pool lit purple at night among palms"></div>
    <div class="gallery__item gallery__item--fire" role="img" aria-label="Photo of a stone-edged pool with fire bowl beside a covered patio"></div>
    <div class="gallery__item gallery__item--lawn" role="img" aria-label="Photo of a raised infinity pool beside a house and lawn at dusk"></div>
  </section>

  <p class="contact">design@kelvaroinc.com <span>|</span> (281) 555-0187 <span>|</span> www.kelvaropools.com</p>
</main>
</body>
</html>
```